Varden Institute for Restorative Care

I need a full informational website for my medical practice. I would like to use my logo and also include a lot of emblems/pictures (also a picture of me in a white coat). The website should have a function for people to inquire and send me messages. I will be offering needle-less regenerative injection therapy, stem cell treatments, bioidentical hormone therapy, treatment for chronic illness, neurodegenerative diseases, skin rejuvenation, hair restoration, male enhancement, female enhancement, and anti-aging. The practice will not be accepting insurance and will be cash/credit card only.
A good example of written content and functionality is this website:
http://thebrvx.example/. However, I want different theme and tones.
Target Market(s)
High end clientele in Los Angeles, Southern California. Health minded people who are interested in living better and longer and can afford anti-aging treatments. Men and women who want to improve sexual health and wellbeing.
Requirements
Must have
- 1. I will need to be able to move the site to other servers (needed for site speed)
- 2. Site must be build on WordPress
- 3. Full admin credentials for domain, cpanel, wordpress, ftp.
- 4. No third party interaction on development and content deployment once the site is on different servers
- 5. I will need the ability to add content and links to the site
- 6. I will need the ability to optimize the site for speed
- 7. I will need to ability to modify URLs so they are more SEO friendly
Nice to have
- pictures of stem cells, health improvement and regeneration, beauty, youthful individuals, older healthy and happy individuals. Medical designs.
Should not have
- flowers, dna

```html
<!DOCTYPE html>
<html lang="en">
<head>
<meta charset="utf-8">
<title>Varden Institute for Restorative Care</title>
<link href="https://fonts.googleapis.com/css2?family=Montserrat:wght@400;500;600;700&display=swap" rel="stylesheet">
<style>
:root{
  --ink:#2b2b2b;
  --muted:#8a8a8a;
  --teal:#7bbfb5;
  --teal-dark:#2f9a8c;
  --sky:#7cc3e3;
  --navy:#1a3366;
  --pale:#eef6f9;
  --line:#d9e3e7;
  --white:#ffffff;
}
*{box-sizing:border-box;margin:0;padding:0}
html,body{width:667px;height:1200px;overflow:hidden;background:var(--white)}
body{position:relative;font-family:"Montserrat",sans-serif;color:var(--ink)}
.abs{position:absolute}
.btn{position:absolute;background:var(--sky);color:var(--white);font-weight:600;display:flex;align-items:center;justify-content:center;font-size:6.5px}

/* header */
.brand{left:133px;top:8px;display:flex;align-items:center;gap:5px}
.brand-dot{width:16px;height:16px;border-radius:50%;background:var(--teal-dark)}
.brand-name{font-size:13px;font-weight:600;color:var(--navy);letter-spacing:.5px}
.nav{right:131px;top:13px;display:flex;gap:11px;font-size:5.8px;font-weight:500}

/* hero */
.hero-art{left:315px;top:36px;width:195px;height:128px;background:radial-gradient(ellipse at center,#efedee 0%,#f6f5f5 55%,#fff 100%)}
.hero-tag{left:138px;top:74px;font-size:4.6px;letter-spacing:.6px;color:#555}
.hero-title{left:138px;top:83px;font-size:13.5px;font-weight:600;line-height:16px;width:200px}
.arrow{top:93px;width:8px;height:14px}
.inquiry{left:138px;top:121px;width:57px;height:17px}

/* neuron band */
.neuron-band{left:0;top:165px;width:667px;height:129px;background:linear-gradient(90deg,#0d2050,#1f4a8a 40%,#16356e 70%,#0c1d48)}

/* welcome */
.welcome{left:0;top:294px;width:667px;height:220px;background:var(--teal)}
.doctor{left:346px;top:278px;width:155px;height:236px;background:linear-gradient(180deg,#c9a68e 0%,#e9eef0 30%,#f4f6f7 100%)}
.welcome-title{left:137px;top:350px;width:200px;font-size:12px;line-height:15px;color:var(--white)}
.welcome-title b{font-weight:600}
.welcome-sub{left:137px;top:387px;font-size:7px;color:var(--white)}
.welcome-text{left:137px;top:398px;width:160px;font-size:4.8px;line-height:6.3px;color:#eaf6f3}
.meet{left:138px;top:450px;width:71px;height:18px;background:#8fd0e6}

/* services */
.tri-field{left:40px;top:596px;width:210px;height:222px;background:linear-gradient(135deg,#fff 0%,#f1f1f1 45%,#e6e6e6 70%,#fafafa 100%)}
.services-title{left:137px;top:563px;font-size:12px;font-weight:600}
.services-intro{left:137px;top:583px;width:100px;font-size:5px;line-height:6.2px;color:#666}
.more{left:137px;top:617px;width:30px;height:11px;font-size:5px}
.service{position:absolute;width:100px}
.service-icon{width:20px;height:20px;border-radius:50%;border:1.2px solid var(--teal);background:#eaf6f3}
.service h3{font-size:5.8px;font-weight:600;margin-top:7px;line-height:7px}
.service p{font-size:4.3px;line-height:6.2px;color:#999;margin-top:5px}

/* contact */
.contact{left:0;top:877px;width:667px;height:231px;background:var(--pale)}
.contact-title{left:0;top:893px;width:667px;text-align:center;font-size:15px;font-weight:700}
.contact-sub{left:0;top:914px;width:667px;text-align:center;font-size:6px;color:#555}
.field{position:absolute;width:160px;border-bottom:.8px solid var(--line);padding-bottom:4px}
.field label{display:block;font-size:5px;font-weight:600}
.field span{display:block;font-size:4.6px;color:#aaa;margin-top:3px}
.submit{left:163px;top:1064px;width:60px;height:16px}

/* footer */
.foot-brand{left:144px;top:1127px}
.copy{left:130px;top:1153px;width:120px;text-align:center;font-size:4.8px;line-height:6px;color:#444}
.foot-head{font-size:8px;font-weight:500;color:#333}
.foot-list{font-size:5px;line-height:9px;color:#444;margin-top:5px}
.socials{display:flex;gap:3px;margin-top:7px}
.social{width:11px;height:11px;border-radius:50%;background:var(--navy)}
</style>
</head>
<body>

<header>
  <div class="abs brand"><span class="brand-dot"></span><span class="brand-name">Varden</span></div>
  <nav class="abs nav"><span>Home</span><span>About</span><span>Services</span><span>Science</span><span>Testimonials</span><span>Dr. Hale Videos</span><span>Contact</span></nav>
</header>

<section class="hero">
  <div class="abs hero-art" role="img" aria-label="Faint molecule cluster decoration"></div>
  <p class="abs hero-tag">IT IS TIME THAT WE GO BACK TO THE ORIGIN</p>
  <h1 class="abs hero-title">Varden Institute is the medicine of the future.</h1>
  <svg class="abs arrow" style="left:112px" viewBox="0 0 8 14"><path d="M7 1 1 7l6 6" fill="none" stroke="#aaa" stroke-width="1"/></svg>
  <svg class="abs arrow" style="left:543px" viewBox="0 0 8 14"><path d="M1 1l6 6-6 6" fill="none" stroke="#aaa" stroke-width="1"/></svg>
  <div class="btn inquiry">Inquiry Now</div>
</section>

<div class="abs neuron-band" role="img" aria-label="Photograph of glowing blue nerve cells"></div>

<section>
  <div class="abs welcome"></div>
  <div class="abs doctor" role="img" aria-label="Photograph of the doctor in a white coat with stethoscope, arms crossed"></div>
  <h2 class="abs welcome-title">Welcome to <b>Varden Institute for Restorative Care</b></h2>
  <p class="abs welcome-sub">CEO of Varden Institute for Restorative Care</p>
  <p class="abs welcome-text">Sed ut perspiciatis unde omnis iste natus error sit voluptatem accusantium doloremque laudantium, totam rem aperiam, eaque ipsa quae ab illo inventore veritatis et quasi architecto beatae vitae dicta sunt explicabo. Nemo enim ipsam voluptatem quia voluptas sit aspernatur aut odit aut fugit, sed quia consequuntur magni dolores eos qui ratione voluptatem sequi nesciunt.</p>
  <div class="btn meet">MEET THE DOCTOR</div>
</section>

<section>
  <div class="abs tri-field" role="img" aria-label="Faint grey triangle pattern decoration"></div>
  <h2 class="abs services-title">Our Services</h2>
  <p class="abs services-intro">Lorem ipsum dolor sit amet, consectetur adipiscing elit, sed do eiusmod tempor incididunt ut labore et dolore magna aliqua.</p>
  <div class="btn more">More</div>

  <div class="service" style="left:283px;top:561px"><div class="service-icon" role="img" aria-label="Crossed-out needle icon"></div><h3>Needleless regenerative<br>injection therapy</h3><p>Lorem ipsum dolor sit amet, consectetur adipiscing elit, sed do eiusmod tempor incididunt ut labore et dolore magna aliqua. Ut enim ad minim veniam, quis nostrud exercitation ullamco.</p></div>
  <div class="service" style="left:412px;top:561px"><div class="service-icon" role="img" aria-label="Stem cell icon"></div><h3>Stem Cell<br>Treatments</h3><p>Lorem ipsum dolor sit amet, consectetur adipiscing elit, sed do eiusmod tempor incididunt ut labore et dolore magna aliqua. Ut enim ad minim veniam, quis nostrud exercitation ullamco.</p></div>
  <div class="service" style="left:283px;top:658px"><div class="service-icon" role="img" aria-label="Hormone molecule icon"></div><h3>Bioidentical hormone therapy<br>&nbsp;</h3><p>Lorem ipsum dolor sit amet, consectetur adipiscing elit, sed do eiusmod tempor incididunt ut labore et dolore magna aliqua. Ut enim ad minim veniam, quis nostrud exercitation ullamco.</p></div>
  <div class="service" style="left:412px;top:658px"><div class="service-icon" role="img" aria-label="Person in discomfort icon"></div><h3>Treatment for chronic<br>illness</h3><p>Lorem ipsum dolor sit amet, consectetur adipiscing elit, sed do eiusmod tempor incididunt ut labore et dolore magna aliqua. Ut enim ad minim veniam, quis nostrud exercitation ullamco.</p></div>
  <div class="service" style="left:283px;top:751px"><div class="service-icon" role="img" aria-label="Brain icon"></div><h3>Neurodegenerative Diseases</h3><p>Lorem ipsum dolor sit amet, consectetur adipiscing elit, sed do eiusmod tempor incididunt ut labore et dolore magna aliqua. Ut enim ad minim veniam, quis nostrud exercitation ullamco.</p></div>
  <div class="service" style="left:412px;top:751px"><div class="service-icon" role="img" aria-label="Face profile icon"></div><h3>Skin Rejuvenation</h3><p>Lorem ipsum dolor sit amet, consectetur adipiscing elit, sed do eiusmod tempor incididunt ut labore et dolore magna aliqua. Ut enim ad minim veniam, quis nostrud exercitation ullamco.</p></div>
</section>

<section>
  <div class="abs contact"></div>
  <h2 class="abs contact-title">CONTACT US</h2>
  <p class="abs contact-sub">Fill out the form to</p>
  <div class="field" style="left:158px;top:941px"><label>FIRST NAME*</label><span>Enter your First name</span></div>
  <div class="field" style="left:353px;top:941px"><label>LAST NAME*</label><span>Enter your Last name</span></div>
  <div class="field" style="left:158px;top:978px"><label>EMAIL ADDRESS*</label><span>Enter your Email Address</span></div>
  <div class="field" style="left:353px;top:978px"><label>PHONE NUMBER*</label><span>Enter your Phone Number</span></div>
  <div class="field" style="left:158px;top:1015px;width:355px;height:36px"><label>NOTES</label><span>Enter Small Discriptions</span></div>
  <div class="btn submit">SUBMIT NOW</div>
</section>

<footer>
  <div class="abs brand foot-brand"><span class="brand-dot"></span><span class="brand-name">Varden</span></div>
  <p class="abs copy">Copyright © 2018 Varden Institute for Restorative Care - All Rights Reserved.</p>
  <div class="abs" style="left:254px;top:1122px"><div class="foot-head">Links</div><div class="foot-list">Home<br>About Us<br>Services<br>What's New<br>Contact</div></div>
  <div class="abs" style="left:326px;top:1122px"><div class="foot-head">Address</div><div class="foot-list" style="line-height:6.5px">4810 Larchmont Ridge Rd<br>Westvale, CA 90000<br><br>+1 555 014 2290</div></div>
  <div class="abs" style="left:443px;top:1122px"><div class="foot-head">Social Media</div><div class="socials"><span class="social"></span><span class="social" style="background:#2e86c9"></span><span class="social" style="background:#2e6fa8"></span></div></div>
</footer>

</body>
</html>
```